ORV NETWORKS LTD

going to a headteacher conference need a sign to show our services:
www.orv-networks.co.uk
will attach a leaflet showing some more information.

Services:
IT Support
Web Design
Data Cabling (Fibre/Cat6)
Broadband
Hardware sales
WIFI
CCTV
Audio Visual
Door Access System
VOIP Telephone

```html
<!DOCTYPE html>
<html lang="en">
<head>
<meta charset="utf-8">
<title>ORV Networks – Conference Banner</title>
<link rel="stylesheet" href="https://fonts.googleapis.com/css2?family=Montserrat:wght@400;500;700&display=swap">
<style>
  :root {
    --orange: #ef7536;
    --orange-dark: #d4521c;
    --blue: #0b5eb3;
    --blue-deep: #0a4f98;
    --navy: #0c1d33;
    --navy-mid: #143a63;
    --ink: #1d1d1f;
    --white: #ffffff;
  }
  * { margin: 0; padding: 0; box-sizing: border-box; }
  html, body { width: 1200px; height: 1200px; overflow: hidden; background: var(--white); }
  body { font-family: "Montserrat", Arial, sans-serif; }

  .banner { position: relative; width: 1200px; height: 1200px; background: var(--white); overflow: hidden; }

  .brand {
    position: absolute; top: 40px; right: 40px;
    display: flex; flex-direction: column; align-items: flex-end;
  }
  .brand-name {
    display: flex; align-items: center; gap: 14px;
    font-weight: 700; font-size: 46px; color: var(--blue); letter-spacing: 1px;
  }
  .brand-square { width: 36px; height: 36px; background: var(--orange); }
  .brand-rule { width: 100%; height: 3px; background: var(--orange); margin-top: 12px; }

  .hero-photo {
    position: absolute; left: 0; top: 150px; width: 1200px; height: 905px;
    background:
      radial-gradient(circle at 62% 52%, rgba(150,200,255,0.55) 0, rgba(60,120,190,0.35) 9%, transparent 22%),
      radial-gradient(circle at 72% 35%, rgba(240,140,60,0.25) 0, transparent 18%),
      radial-gradient(ellipse at 25% 75%, rgba(190,120,90,0.35) 0, transparent 35%),
      linear-gradient(135deg, var(--navy-mid) 0%, var(--navy) 55%, #0a1526 100%);
  }

  .headline-tab { position: absolute; left: 0; top: 45px; width: 560px; height: 390px; }
  .headline {
    position: absolute; left: 50px; top: 100px;
    color: var(--white); font-weight: 700; font-size: 54px; line-height: 72px;
    text-transform: uppercase; letter-spacing: 0.5px;
  }

  .services {
    position: absolute; left: 0; top: 815px; width: 705px; height: 308px;
    background: linear-gradient(90deg, var(--blue-deep), var(--blue));
    display: flex; padding: 30px 0 0 50px;
  }
  .service-list { list-style: none; }
  .service-list li {
    display: flex; align-items: center; gap: 14px;
    color: var(--white); font-size: 24px; font-weight: 400; height: 43px;
  }
  .service-list--left { width: 335px; }
  .service-list--right { padding-left: 38px; border-left: 2px solid rgba(255,255,255,0.6); padding-top: 10px; height: 230px; }
  .service-list--right li { font-size: 25px; }
  .tick { width: 18px; height: 18px; flex: none; }

  .web-address {
    position: absolute; right: 42px; top: 1115px;
    font-size: 33px; font-weight: 500; color: var(--ink);
  }
</style>
</head>
<body>
<main class="banner">
  <svg width="0" height="0" style="position:absolute">
    <symbol id="tick" viewBox="0 0 20 20">
      <path d="M3 10.5 L8 15.5 L17.5 4.5" fill="none" stroke="#ffffff" stroke-width="3" stroke-linecap="round" stroke-linejoin="round"/>
    </symbol>
  </svg>

  <div class="hero-photo" role="img" aria-label="Photo of hands at a laptop holding a glowing globe surrounded by connected people icons on a dark blue network background"></div>

  <svg class="headline-tab" viewBox="0 0 560 390" aria-hidden="true">
    <polygon points="0,0 470,0 560,130 560,390 0,390" fill="var(--orange-dark)"/>
    <path d="M0 0 H470 L500 40 V350 Q500 390 460 390 H0 Z" fill="var(--orange)"/>
  </svg>
  <h1 class="headline">SLA Services<br>&amp; Internet<br>Connectivity<br>Services</h1>

  <header class="brand">
    <div class="brand-name"><span class="brand-square"></span>ORV NETWORKS LTD</div>
    <div class="brand-rule"></div>
  </header>

  <section class="services" aria-label="Services">
    <ul class="service-list service-list--left">
      <li><svg class="tick"><use href="#tick"/></svg>IT Support</li>
      <li><svg class="tick"><use href="#tick"/></svg>Web Design</li>
      <li><svg class="tick"><use href="#tick"/></svg>Data Cabling (Fibre/Cat6)</li>
      <li><svg class="tick"><use href="#tick"/></svg>Broadband</li>
      <li><svg class="tick"><use href="#tick"/></svg>Hardware sales</li>
    </ul>
    <ul class="service-list service-list--right">
      <li><svg class="tick"><use href="#tick"/></svg>WIFI</li>
      <li><svg class="tick"><use href="#tick"/></svg>CCTV</li>
      <li><svg class="tick"><use href="#tick"/></svg>Audio Visual</li>
      <li><svg class="tick"><use href="#tick"/></svg>Door Access System</li>
      <li><svg class="tick"><use href="#tick"/></svg>VOIP Telephone</li>
    </ul>
  </section>

  <p class="web-address">www.orv-networks.co.uk</p>
</main>
</body>
</html>
```